"The Craft of Patron Care," fourth edition cover design

Later this year, my publisher, Harold Penmarsh & Daughters, will issue a fourth, substantially revised edition of "The Craft of Patron Care," following the 2016 publication of the third edition and the second and first versions that were issued earlier.

To distinguish this new edition from previous ones, I need a cover design that visually connects and is consistent with what has preceded it, while signaling this is a new and different, worthy of prospective readers/buyers’ attention.

Attached are three different verbal approaches to the new cover; these are NOT MEANT to serve as actual designs, but rather will give you a sense of how language is to be deployed:

The first emphasizes “ART” as the key visual word in the book title;
The second emphasizes “CLIENT SERVICE” as the key visual words in the book title; and,
The third emphasizes just the word "CLIENT" in the book title.

A top-of-the-page is a pre-head that applies to all three versions:
“6 TIMELESS PRINCIPLES FOR ADVERTISING & MARKETING PRO’s
IN AN AI WORLD"

There's a mid-page sub-head for all three versions:
“THE CLASSIC GUIDE,” followed by
“FOURTH EDITION BY GERALD ASHCOMBE

And there's a one-line, bottom-of-the-page designation:
“Foreword by Mae Dunford, Global Executive Creative Director, Starbolt"

The pallette for the previously published third edition was black with red as an accent color on a field of white; I've attached a sample for reference, so you can see how it was executed. For this new fourth edition, I'd like to change the accent color from red to either Wedgewood blue, or British racing green, or an alternative that is assertive and color saturated -- think of primary colors -- that contrast sufficiently with the base of black. As an alternative, you can consider a cover that used either Wedgewood blue, British racing green, or another possibility as a full-bleed field, with copy content either revered out or surprinted.

Lastly, while the new cover largely is meant to be typographically driven, if you can come up with a visual metaphor that illustrates and builds on the book's title, that would be very helpful. By way of reference, the third edition's book cover attempted to do this by introducing a visual element at the end of the book's title that's meant to represent an artist's paint splatter (although I admit it didn't work as well as it should).

Target Market(s)

Prospective purchasers of the book who might discover copies at a bookstore, but more likely will encounter it through online distributors such as Riverdex, Hartwell & Pike, and Tindall’s.

Industry/Entity Type

Advertising and marketing

Font styles to use
Serif
Sans Serif
Other font styles liked:
• A mix of serif and san-serif typefaces is okay. for the examples I shared, I relieid on "Arial Rounded Bold" but you need not be weeded to this. If you opt to mix in a serif font, I am partial to Cambria as a typeface.

Requirements
Must have
• To achieve the goal of being “connected with but distinct” from previous editions, the new cover should be:  Largely typographic, but displaying a color palette different from the previous editions’ black-plus-red-accent on a canvas of white.  Any new accent color selected for use should be vibrant, strong, and highly saturated; think “British racing green,” “Wedgewood blue,” or their equivalents.  In addition to a powerful, “billboard” approach to type and color, consider other visual metaphors that are likely to engage the readers. The winning cover design will stand out from other books, while connecting with the previously published third edition.
Nice to have
• If you can find way to illustrate the book's title through a visual metaphor, that would be ideal.a
Should not have
• Anything that is frivolous or non-sensical

```html
<!DOCTYPE html>
<html lang="en">
<head>
<meta charset="utf-8">
<title>The Craft of Patron Care — Fourth Edition Cover</title>
<link rel="stylesheet" href="https://fonts.googleapis.com/css2?family=Anton&family=Bebas+Neue&family=Montserrat:wght@400;500;700&display=swap">
<style>
  :root {
    --page: #ecebf0;
    --paper: #ffffff;
    --green: #0b432a;
    --ink: #2b2a2b;
    --display: "Bebas Neue", "Oswald", sans-serif;
    --heavy: "Anton", "Impact", sans-serif;
    --body: "Montserrat", "Helvetica Neue", Arial, sans-serif;
  }
  * { margin: 0; padding: 0; box-sizing: border-box; }
  html, body {
    width: 1200px; height: 1200px; overflow: hidden;
    background: var(--page);
  }
  .cover {
    position: absolute; left: 200px; top: 0;
    width: 800px; height: 1200px;
    background: var(--paper);
    font-family: var(--body);
    color: var(--ink);
  }
  .prehead {
    position: absolute; left: 67px; top: 72px;
    font-size: 19.5px; line-height: 25px; font-weight: 400;
  }
  .prehead strong { color: var(--green); font-weight: 700; display: block; }
  .rule-vertical {
    position: absolute; left: 68px; top: 145px;
    width: 2px; height: 461px; background: var(--green);
  }
  .title-art { position: absolute; left: 0; top: 0; width: 800px; height: 1200px; }
  .title-art .t-the { font-family: var(--display); fill: var(--ink); }
  .title-art .t-craft { font-family: var(--heavy); fill: var(--green); }
  .title-art .t-of { font-family: var(--display); fill: var(--green); }
  .title-art .t-patron { font-family: var(--display); fill: var(--green); }
  .title-art .t-care { font-family: var(--display); fill: var(--ink); }
  .edition-label {
    position: absolute; left: 99px; top: 982px;
    font-size: 12.5px; font-weight: 500; letter-spacing: 3.2px;
  }
  .edition-name {
    position: absolute; left: 98px; top: 1000px;
    font-family: var(--display); font-size: 42px; line-height: 42px;
    letter-spacing: 2.6px; color: var(--green);
  }
  .byline {
    position: absolute; left: 100px; top: 1049px;
    font-size: 13px; font-weight: 500; letter-spacing: 3.6px;
  }
  .byline .author { color: var(--green); font-weight: 700; margin-left: 4px; }
  .rule-horizontal {
    position: absolute; left: 338px; top: 1055px;
    width: 462px; height: 2px; background: var(--green);
  }
  .foreword {
    position: absolute; right: 71px; top: 1120px;
    font-size: 12.5px; line-height: 20px; text-align: right;
  }
</style>
</head>
<body>
  <main class="cover">
    <p class="prehead">
      <strong>6 TIMELESS PRINCIPLES</strong>
      FOR ADVERTISING &amp; MARKETING PRO’s<br>IN AN AI WORLD
    </p>
    <div class="rule-vertical"></div>

    <svg class="title-art" viewBox="0 0 800 1200" role="img" aria-label="The Craft of Patron Care">
      <text class="t-the" x="342" y="408" font-size="80" textLength="120" lengthAdjust="spacing">THE</text>
      <text class="t-of" x="208" y="721" font-size="84" textLength="64" lengthAdjust="spacingAndGlyphs">OF</text>
      <text class="t-craft" x="284" y="721" font-size="345" textLength="353" lengthAdjust="spacingAndGlyphs">CRAFT</text>
      <text class="t-patron" x="165" y="839" font-size="141" textLength="277" lengthAdjust="spacingAndGlyphs">PATRON</text>
      <text class="t-care" x="458" y="795" font-size="80" textLength="78" lengthAdjust="spacingAndGlyphs">CA</text>
      <text class="t-care" x="538" y="843" font-size="80" textLength="99" lengthAdjust="spacingAndGlyphs">RE</text>
    </svg>

    <p class="edition-label">THE CLASSIC GUIDE</p>
    <p class="edition-name">FOURTH EDITION</p>
    <p class="byline">BY <span class="author">GERALD ASHCOMBE</span></p>
    <div class="rule-horizontal"></div>

    <p class="foreword">Foreword by Mae Dunford, Global Executive<br>Creative Director, Starbolt</p>
  </main>
</body>
</html>
```